Design for a Note buying company that attracts landlords and seller financed notes

I need a card designed. I want a simple clean front with my logo and contact info. On the back I want some big and bold words to get a message across.

Our Company buys Notes (mortgages) and we want to convey the sense of financial security. Our number one market that we pursue is tired landlords.

If you want to understand our business you can visit our website. www.larkpapertrust.com

Do not use any Clip Art in the design, it will not be accepted. I want a custom designed card not something I could throw together myself. Simple clean and drive the message home.

Target Market(s)

Landlords, seller financed note holders

Industry/Entity Type

Mortgage

Contact Information for Business Card

Simple clean and bold. I need to grab the attention of the customer. It should convey a professional touch.

Font styles to use
Sans Serif

Colors
ec2229
ffffff

Requirements
Must have
• Clean front with logo and contact information
Front colors should match logo

Back should be bold and grab attention. Back colors are open to ideas
Nice to have
• The Back May use the phrase "No more Tentants, No more Toilets" "More Time, More Cash"

I'm open to other ideas about grabbing a landlords attention

I'm open to a square card design
I like cards with round corners as well
Should not have
• any clip art! must be custom designs.

```html
<!DOCTYPE html>
<html lang="en">
<head>
<meta charset="utf-8">
<title>Lark Paper Trust – Business Card</title>
<link rel="stylesheet" href="https://fonts.googleapis.com/css2?family=Montserrat:wght@600;700;800&family=Roboto:wght@400&display=swap">
<style>
  :root {
    --brand-red: #ec2229;
    --ink: #0b0b0b;
    --text-grey: #333333;
    --paper: #ffffff;
    --backdrop: #dedede;
    --back-black: #05070a;
    --back-warm: #170b0b;
  }
  * { box-sizing: border-box; margin: 0; padding: 0; }
  html, body { width: 1173px; height: 1200px; overflow: hidden; }
  body { background: var(--backdrop); position: relative; font-family: "Roboto", Arial, sans-serif; }

  .card { position: absolute; left: 205px; width: 742px; height: 411px; }
  .card-front { top: 150px; background: var(--paper); }
  .card-back { top: 637px; background: var(--back-black); overflow: hidden; }

  .tagline {
    position: absolute; top: 44px; left: 0; width: 100%; text-align: center;
    font-family: "Montserrat", Arial, sans-serif; font-weight: 700;
    font-size: 12px; letter-spacing: 6px; color: var(--ink);
  }
  .brand {
    position: absolute; top: 92px; left: 0; width: 100%;
    display: flex; justify-content: center; align-items: center; gap: 12px;
  }
  .brand-mark { width: 22px; height: 22px; background: var(--brand-red); }
  .brand-name {
    font-family: "Montserrat", Arial, sans-serif; font-weight: 800;
    font-size: 40px; letter-spacing: 1px; color: var(--ink);
  }

  .person { position: absolute; right: 400px; top: 234px; text-align: right; font-family: "Montserrat", Arial, sans-serif; }
  .person-name { font-weight: 700; font-size: 25px; color: var(--ink); letter-spacing: -0.3px; }
  .person-role { font-weight: 700; font-size: 21px; color: var(--brand-red); margin-top: 0; }

  .divider { position: absolute; left: 371px; top: 223px; width: 2px; height: 87px; background: var(--ink); }

  .contact { position: absolute; left: 399px; top: 219px; list-style: none; }
  .contact li { display: flex; align-items: center; height: 30px; font-size: 24px; color: var(--text-grey); }
  .contact svg { width: 22px; height: 22px; margin-right: 8px; flex: none; }

  .address {
    position: absolute; top: 332px; left: 0; width: 100%; text-align: center;
    font-size: 23px; color: var(--text-grey);
  }

  .back-art {
    position: absolute; inset: 0;
    background: linear-gradient(90deg, var(--back-warm) 0%, var(--back-warm) 35%, var(--back-black) 75%);
  }
  .slogan {
    position: absolute; top: 138px; left: 0; width: 100%; text-align: center;
    font-family: "Montserrat", Arial, sans-serif; font-weight: 700;
    font-size: 34px; line-height: 43px; color: var(--brand-red); letter-spacing: -0.5px;
  }
</style>
</head>
<body>
  <section class="card card-front">
    <p class="tagline">WE HELP PEOPLE LIVE!</p>
    <div class="brand">
      <span class="brand-mark"></span>
      <span class="brand-name">LARK PAPER TRUST</span>
    </div>

    <div class="person">
      <p class="person-name">MARION HALE</p>
      <p class="person-role">Founder</p>
    </div>
    <div class="divider"></div>

    <ul class="contact">
      <li>
        <svg viewBox="0 0 24 24" aria-hidden="true"><path fill="#ec2229" d="M2 9c0-3 4-5 10-5s10 2 10 5v2h-5V8.5c-1.5-.6-3.2-.8-5-.8s-3.5.2-5 .8V11H2zm4 3 2-3h8l2 3v8H6zm6 1.5a2.5 2.5 0 1 0 0 5 2.5 2.5 0 0 0 0-5z"/></svg>
        555.210.4470
      </li>
      <li>
        <svg viewBox="0 0 24 24" aria-hidden="true"><rect x="2" y="5" width="20" height="14" fill="#ec2229"/><path d="M2 5l10 8 10-8M2 19l8-7M22 19l-8-7" stroke="#fff" stroke-width="1.5" fill="none"/></svg>
        info@larkpapertrust.com
      </li>
      <li>
        <svg viewBox="0 0 24 24" aria-hidden="true"><circle cx="12" cy="12" r="10" fill="#ec2229"/><path d="M8 5c2 1 1 3 3 4s0 3-2 3-2 3 0 5M15 4c-1 2 1 3 3 3M17 13c-2 0-3 2-2 4" stroke="#fff" stroke-width="1.6" fill="none"/></svg>
        www.larkpapertrust.com
      </li>
    </ul>

    <p class="address">48 Alder Crest Road, Marlow Bay, ON L0X 1K4</p>
  </section>

  <section class="card card-back">
    <div class="back-art" role="img" aria-label="Faint dark-red house silhouette decoration on black"></div>
    <p class="slogan">"NO MORE TENTANTS,<br>NO MORE TOILETS"<br>"MORE TIME, MORE CASH"</p>
  </section>
</body>
</html>
```